PREMIUM AGENCY High End Business Card - A+++ Designers Wanted

** DO NOT ATTEMPT TO CONTACT ME THROUGH SEARCHING ON GOOGLE OR EMAILING ME THROUGH MY WEBSITE **

I need a fresh, contemporary business card designed using the logo attached (VOLKRANE)

I have attached the font for VOLKRANE

It must have a premium look and feel. The business card size must be STANDARD size.

You can submit either/both VERTICAL or HORIZONTAL designs.

FRONT: It must have the following sample information on

Peter Dowle
Director Operations
Mobile +61 452 000 000
Email peterdowle@volkrane.example
www.volkrane.example

The REAR of the business card must have the words

CREATE INSPIRE TOMORROW

as part of the design, in the same font (NEXA) attached.

The words do not need to be in capitals, or on the same line, please design this as you see it best working.

ADDITIONAL INFORMATION
======================

The VOLKRANE logo must be on the front of the card

I want Ultraviolet printing on the final design, to enhance either the NAME of the person OR the VOLKRANE logo OR the words on the back of the card.

Target Market(s)

Agency, Advertising Agency, Creative, Designers

Industry/Entity Type

Media

Contact Information for Business Card

Design Agency, Contemporary, Premium look and feel, High Quality

Font styles to use
Serif
Sans Serif
Other font styles liked:
• ATTACHED TO PROJECT

Requirements
Must have
• BLACK & WHITE as the primary design, and if you feel there can be a highlighted colour, then this can be used.
• The Logo ICON attached is blue, this colour must not be changed.
• I have attached the partner brand VOLKRANE MEDIA incase you need to manipulate the original files.
• ** DO NOT ATTEMPT TO CONTACT ME THROUGH SEARCHING ON GOOGLE OR EMAILING ME THROUGH MY WEBSITE **
Nice to have
• Must be Premium. I have attached some sample designs, that I like that would be a good inspiration for where this can be taken.
• My favourite design is is the SNAPFRAME2-BUSINESSCARD-TEMPLATE
Should not have
• No funny or silly standard / off the shelf designs

```html
<!DOCTYPE html>
<html lang="en">
<head>
<meta charset="utf-8">
<title>VOLKRANE – Business Card</title>
<link rel="stylesheet" href="https://fonts.googleapis.com/css2?family=Montserrat:wght@500;600&family=Quicksand:wght@400;500;600&display=swap">
<style>
  :root {
    --backdrop: #565657;
    --card: #3c3c3d;
    --brand-blue: #22a3dd;
    --ink-black: #141414;
    --text-white: #f4f4f4;
    --brand-font: "Montserrat", sans-serif;
    --body-font: "Quicksand", sans-serif;
  }
  * { box-sizing: border-box; margin: 0; padding: 0; }
  html, body {
    width: 1200px; height: 796px; overflow: hidden;
    background: var(--backdrop);
  }
  .canvas {
    position: relative; width: 1200px; height: 796px;
    display: flex; align-items: center; justify-content: center; gap: 40px;
  }
  .card {
    position: relative; width: 540px; height: 330px;
    background: var(--card); overflow: hidden;
    box-shadow: 0 14px 30px rgba(0,0,0,.35);
  }
  .card-band { position: absolute; inset: 0; width: 100%; height: 100%; }
  .band-fill { fill: var(--brand-blue); }

  .wordmark {
    position: absolute; display: flex; align-items: center;
    font-family: var(--brand-font); font-weight: 600;
    color: var(--ink-black); letter-spacing: .06em;
  }
  .wordmark-dot {
    display: inline-block; border-radius: 50%;
    background: var(--brand-blue);
  }
  .back .wordmark { left: 58px; top: 92px; font-size: 62px; gap: 18px; }
  .back .wordmark-dot { width: 30px; height: 30px; }
  .front .wordmark { left: 30px; top: 34px; font-size: 40px; gap: 12px; }
  .front .wordmark-dot { width: 20px; height: 20px; }

  .tagline {
    position: absolute; display: flex; align-items: center; gap: 10px;
    font-family: var(--body-font); font-weight: 500; font-size: 19px;
    color: var(--text-white);
  }
  .tagline::before, .tagline::after {
    content: ""; width: 30px; height: 1.5px; background: var(--text-white);
  }
  .back .tagline { left: 20px; top: 284px; }
  .front .tagline { right: 20px; top: 284px; }

  .website-back {
    position: absolute; right: 28px; top: 276px;
    font-family: var(--body-font); font-weight: 600; font-size: 14px;
    color: var(--ink-black);
  }

  .person {
    position: absolute; right: 300px; top: 146px; text-align: right;
    font-family: var(--body-font);
  }
  .person-name { font-size: 31px; font-weight: 600; color: var(--text-white); line-height: 1.1; }
  .person-role { font-size: 16px; font-weight: 400; color: var(--brand-blue); margin-top: 2px; }

  .divider {
    position: absolute; left: 262px; top: 128px;
    width: 1.5px; height: 104px; background: var(--brand-blue);
  }

  .contacts {
    position: absolute; left: 282px; top: 140px; list-style: none;
    font-family: var(--body-font); font-weight: 500; font-size: 14px;
    color: var(--text-white);
  }
  .contacts li { display: flex; align-items: center; gap: 9px; height: 26px; }
  .contact-icon { width: 14px; height: 14px; flex: none; }
  .contact-icon * { stroke: var(--brand-blue); fill: none; stroke-width: 1.6; }
  .contact-icon .solid { fill: var(--brand-blue); stroke: none; }
</style>
</head>
<body>
<main class="canvas">

  <section class="card back" aria-label="Card back">
    <svg class="card-band" viewBox="0 0 540 330" aria-hidden="true">
      <path class="band-fill" d="M0 268 H300 C330 268 338 308 372 308 H540 V330 H0 Z"/>
    </svg>
    <div class="wordmark"><span class="wordmark-dot"></span>VOLKRANE</div>
    <p class="website-back">www.volkrane.example</p>
    <p class="tagline">Create inspire tomorrow</p>
  </section>

  <section class="card front" aria-label="Card front">
    <svg class="card-band" viewBox="0 0 540 330" aria-hidden="true">
      <path class="band-fill" d="M0 310 H250 C284 310 292 268 324 268 H540 V330 H0 Z"/>
    </svg>
    <div class="wordmark"><span class="wordmark-dot"></span>VOLKRANE</div>

    <div class="person">
      <p class="person-name">Peter Dowle</p>
      <p class="person-role">Director Operations</p>
    </div>
    <span class="divider"></span>

    <ul class="contacts">
      <li>
        <svg class="contact-icon" viewBox="0 0 14 14" aria-hidden="true">
          <rect x="3.5" y="1" width="7" height="12" rx="1.2"/>
          <rect class="solid" x="6" y="10.5" width="2" height="1.2"/>
        </svg>
        +61 452 000 000
      </li>
      <li>
        <svg class="contact-icon" viewBox="0 0 14 14" aria-hidden="true">
          <rect x="1" y="3" width="12" height="8.5" rx="1"/>
          <path d="M1.5 3.5 L7 8 L12.5 3.5"/>
        </svg>
        peterdowle@volkrane.example
      </li>
      <li>
        <svg class="contact-icon" viewBox="0 0 14 14" aria-hidden="true">
          <circle cx="7" cy="7" r="5.8"/>
          <ellipse cx="7" cy="7" rx="2.6" ry="5.8"/>
          <path d="M1.2 7 H12.8 M2.2 4 H11.8 M2.2 10 H11.8"/>
        </svg>
        www.volkrane.example
      </li>
    </ul>

    <p class="tagline">Create inspire tomorrow</p>
  </section>

</main>
</body>
</html>
```